VALMIK GROUP

This is a company that provides executive protection. Our motto is "New Era in Protection"... I don't want this to look like other security websites. I want it to be clean and sharp and represent a new era. We are based in the bay area so maybe a picture of San Francisco in the background?
I want it to be able to funnel down a couple different categories.
1. About Us
2. Services (Executive Protection, Covert Protection, Residential Protection & Intelligence)
3. Blue Pike (Training & Consulting)
4. Contact Us
I want it to be very clean and modern. I don't want there to be any pictures of bodyguards with ear pieces like every other website.
Target Market(s)
Ultra High Net Worth Individuals
Coding
Coded - Design and coding required
Number of Pages Required
1 page
Requirements
Must have
- Colors of my Symbol
Nice to have
- City in the background, San Francisco, New York or the Thornmeadow Club in Montana.
Should not have
- Should not look like an KVM website or have photos of bodyguards. I want this to be a clean and simple website with my logo

```html
<!DOCTYPE html>
<html lang="en">
<head>
<meta charset="UTF-8">
<title>VALMIK GROUP — New Era in Protection</title>
<link rel="stylesheet" href="https://fonts.googleapis.com/css2?family=Lato:wght@300;400;700&family=Saira:wght@300;400&display=swap">
<style>
:root{
  --red:#8c0a0d;
  --red-dark:#6e0709;
  --ink:#222;
  --text:#444;
  --muted:#888;
  --line:#e6e6e6;
  --soft:#f5f5f5;
  --white:#fff;
  --black:#050505;
}
*{box-sizing:border-box;margin:0;padding:0}
html,body{width:1200px;height:3911px;overflow:hidden}
body{position:relative;font-family:'Lato',sans-serif;color:var(--ink);background:var(--white)}
.abs{position:absolute}
a{color:inherit;text-decoration:none}

/* hero */
.hero{position:absolute;left:0;top:0;width:1200px;height:645px;overflow:hidden;
  background:linear-gradient(180deg,#545b64 0%,#646b73 40%,#6a6e70 62%,#8a8b86 100%)}
.hero-subject{position:absolute;left:690px;top:95px;width:510px;height:550px;
  background:linear-gradient(180deg,rgba(30,30,32,.0) 0%,rgba(25,25,28,.55) 35%,rgba(20,20,22,.85) 100%)}
.hero-curve{position:absolute;left:0;bottom:0}
.brand-box{position:absolute;left:182px;top:0;width:119px;height:97px;background:var(--white);
  display:flex;align-items:center;justify-content:center;flex-direction:column;gap:4px}
.brand-box .mark{width:16px;height:16px;background:var(--red)}
.brand-box .name{font-weight:700;font-size:13px;color:var(--red);letter-spacing:.5px}
.nav{position:absolute;top:40px;left:0;font-size:14px;color:var(--white)}
.nav a{position:absolute;white-space:nowrap}
.nav .active{border-bottom:1px solid var(--white);padding-bottom:6px}
.caret{display:inline-block;border:3px solid transparent;border-top:4px solid var(--white);margin-left:4px;vertical-align:1px}
.hero-kicker{left:182px;top:235px;font-size:12px;color:var(--white)}
.hero-title{left:180px;top:258px;font-family:'Saira',sans-serif;font-weight:300;font-size:38px;color:var(--white)}
.hero-text{left:182px;top:337px;width:480px;font-size:12px;line-height:25px;color:var(--white)}
.btn{position:absolute;display:flex;align-items:center;justify-content:center;font-size:12px;border-radius:4px}
.btn-fill{background:var(--red);color:var(--white)}
.btn-line{border:1.5px solid var(--red);color:var(--red);background:var(--white)}

/* about */
.photo{position:absolute;border-radius:4px}
.kicker{font-size:12px;color:var(--ink)}
.h2{font-weight:300;font-size:27px;line-height:38px;color:#333}
.body{font-size:12.5px;line-height:24.6px;color:var(--text)}

/* services */
.services-band{position:absolute;left:0;top:1299px;width:1200px;height:688px;background:var(--soft)}
.arrow-btn{position:absolute;width:37px;height:37px;border-radius:3px;display:flex;align-items:center;justify-content:center}
.arrow-btn.prev{background:var(--white);box-shadow:0 2px 6px rgba(0,0,0,.06)}
.arrow-btn.next{background:var(--red)}
.card{position:absolute;top:1584px;width:263px;height:316px;background:var(--white);border-radius:4px}
.card.active{box-shadow:0 6px 20px rgba(0,0,0,.08)}
.card .icon{position:absolute;left:22px;top:37px;width:88px;height:88px;border-radius:50%;background:#f4f4f4;
  display:flex;align-items:center;justify-content:center}
.card.active .icon{background:var(--red)}
.card h3{position:absolute;left:22px;top:152px;font-weight:400;font-size:19px;color:#222;white-space:nowrap}
.card p{position:absolute;left:22px;top:188px;width:230px;font-size:12px;line-height:24px;color:var(--muted);white-space:nowrap;overflow:hidden}
.card .go{position:absolute;left:22px;top:262px}

/* blue pike */
.h3{font-weight:300;font-size:21px;color:#333}

/* contact */
.contact-row{position:absolute;left:182px;display:flex;gap:12px;align-items:flex-start;font-size:13px;color:var(--text);line-height:22px}
.dot-icon{width:22px;height:22px;border-radius:50%;background:var(--red);flex:none;display:flex;align-items:center;justify-content:center}

/* footer */
.footer-bg{position:absolute;left:0;top:3500px;width:1200px;height:411px}
.foot-title{position:absolute;font-size:14px;color:var(--white);white-space:nowrap}
.foot-link{position:absolute;font-size:12.5px;color:#ddd;white-space:nowrap}
.foot-brand{position:absolute;left:182px;top:3670px;display:flex;align-items:center;gap:10px}
.foot-brand .mark{width:30px;height:30px;border:2px solid #bbb;border-radius:50%;flex:none}
.foot-brand .name{font-size:21px;font-weight:700;color:#ccc;letter-spacing:.5px;white-space:nowrap}
.subscribe{position:absolute;left:785px;top:3667px;width:230px;height:40px;display:flex;border-radius:3px;overflow:hidden}
.subscribe span{flex:1;background:var(--white);font-size:10px;color:#aaa;display:flex;align-items:center;padding-left:16px}
.subscribe b{width:70px;background:var(--red-dark);color:var(--white);font-weight:400;font-size:12px;display:flex;align-items:center;justify-content:center}
.social{position:absolute;top:3738px;width:16px;height:16px;border-radius:50%;background:#ddd}
.foot-rule{position:absolute;left:182px;top:3835px;width:833px;height:1px;background:#333}
.copy{position:absolute;left:0;top:3854px;width:1200px;text-align:center;font-size:10px;color:#999}
</style>
</head>
<body>

<!-- HERO -->
<header class="hero" role="img" aria-label="Bay area coastline with a suspension bridge behind a man in a dark suit with crossed arms">
  <div class="hero-subject"></div>
  <svg class="hero-curve" width="1200" height="645" viewBox="0 0 1200 645">
    <path d="M0 592 Q560 690 1200 530 L1200 645 L0 645Z" fill="var(--red)"/>
    <path d="M0 592 Q560 660 1200 558 L1200 645 L0 645Z" fill="var(--white)"/>
  </svg>
</header>
<div class="brand-box"><span class="mark"></span><span class="name">VALMIK GROUP</span></div>
<nav class="nav">
  <a class="active" style="left:503px">Home</a>
  <a style="left:579px">About Us</a>
  <a style="left:679px">Services<span class="caret"></span></a>
  <a style="left:775px">Blue Pike<span class="caret"></span></a>
  <a style="left:871px">Contact Us</a>
</nav>
<div class="abs hero-kicker">Welcome To</div>
<h1 class="abs hero-title">New Era in Protection.</h1>
<p class="abs hero-text">Lorem ipsum dolor sit amet, consectetur adipiscing elit, sed do eiusmod tempor incididunt ut labore et dolore magna aliqua.</p>
<a class="btn btn-fill" style="left:182px;top:422px;width:125px;height:44px">Read More</a>

<!-- ABOUT -->
<div class="photo" style="left:202px;top:737px;width:386px;height:458px;background:linear-gradient(135deg,#c9cdd1,#9aa0a6 55%,#4b5563)" role="img" aria-label="Man in a white shirt and face mask holding a blazer outside a stone building"></div>
<div class="abs kicker" style="left:633px;top:813px">About Us</div>
<h2 class="abs h2" style="left:633px;top:840px;width:380px">This is a company that provides executive protection</h2>
<p class="abs body" style="left:633px;top:939px;width:362px">Lorem ipsum dolor sit amet, consectetur adipisicing elit, sed do eiusmod tempor incididunt ut labore et dolore magna aliqua. Ut enim ad minim veniam, quis nostrud exercitation ullamco laboris nisi ut aliquip ex ea commodo consequat. Duis aute irure dolor in reprehenderit in voluptate velit esse cillum dolore eu fugiat nulla pariatur. Excepteur sint occaecat cupidatat non proident.</p>
<a class="btn btn-line" style="left:633px;top:1150px;width:130px;height:44px">Know More</a>

<!-- SERVICES -->
<section class="services-band"></section>
<div class="abs kicker" style="left:182px;top:1381px">Services</div>
<h2 class="abs h2" style="left:180px;top:1407px;width:370px">Ut enim ad minim veniam quis nostrud exercitation ullamco laboris</h2>
<p class="abs body" style="left:588px;top:1384px;width:420px;font-size:12px">Duis aute irure dolor in reprehenderit in voluptate velit esse cillum dolore eu fugiat nulla pariatur. Excepteur sint occaecat cupidatat non proident.</p>
<div class="arrow-btn prev" style="left:919px;top:1482px"><svg width="10" height="10" viewBox="0 0 10 10"><path d="M6.5 1.5 3 5l3.5 3.5" fill="none" stroke="#999" stroke-width="1.2"/></svg></div>
<div class="arrow-btn next" style="left:977px;top:1482px"><svg width="10" height="10" viewBox="0 0 10 10"><path d="M3.5 1.5 7 5 3.5 8.5" fill="none" stroke="#fff" stroke-width="1.6"/></svg></div>

<div class="card active" style="left:182px">
  <div class="icon"><svg width="44" height="48" viewBox="0 0 44 48"><path d="M22 3 39 9v14c0 12-8 19-17 22C13 42 5 35 5 23V9Z" fill="none" stroke="#fff" stroke-width="2.2"/><circle cx="22" cy="20" r="5" fill="none" stroke="#fff" stroke-width="1.8"/><path d="M13 34c2-5 5-7 9-7s7 2 9 7" fill="none" stroke="#fff" stroke-width="1.8"/></svg></div>
  <h3>Executive Protection</h3>
  <p>Lorem ipsum dolor sit amet,<br>consectetur adipiscing elit seddo...</p>
  <svg class="go" width="34" height="20" viewBox="0 0 34 20"><path d="M1 10h31M23 2l9 8-9 8" fill="none" stroke="var(--red)" stroke-width="1.6"/></svg>
</div>
<div class="card" style="left:468px">
  <div class="icon"><svg width="42" height="44" viewBox="0 0 42 44"><rect x="6" y="4" width="24" height="32" rx="2" fill="none" stroke="var(--red)" stroke-width="1.6"/><path d="M11 12h14M11 18h14M11 24h8" stroke="var(--red)" stroke-width="1.4"/><rect x="24" y="26" width="13" height="11" rx="1.5" fill="#fff" stroke="var(--red)" stroke-width="1.6"/><path d="M27 26v-3a3.5 3.5 0 0 1 7 0v3" fill="none" stroke="var(--red)" stroke-width="1.6"/></svg></div>
  <h3>Covert Protection</h3>
  <p>Lorem ipsum dolor sit amet,<br>consectetur adipiscing elit seddo...</p>
  <svg class="go" width="34" height="20" viewBox="0 0 34 20"><path d="M1 10h31M23 2l9 8-9 8" fill="none" stroke="#aaa" stroke-width="1.4"/></svg>
</div>
<div class="card" style="left:753px">
  <div class="icon"><svg width="46" height="42" viewBox="0 0 46 42"><path d="M4 20 23 5l19 15" fill="none" stroke="var(--red)" stroke-width="1.8"/><path d="M9 17v20h28V17" fill="none" stroke="var(--red)" stroke-width="1.6"/><rect x="19" y="25" width="8" height="12" fill="none" stroke="var(--red)" stroke-width="1.4"/><circle cx="23" cy="17" r="3.5" fill="none" stroke="var(--red)" stroke-width="1.4"/></svg></div>
  <h3>Residential Protection</h3>
  <p>Lorem ipsum dolor sit amet,<br>consectetur adipiscing elit seddo...</p>
  <svg class="go" width="34" height="20" viewBox="0 0 34 20"><path d="M1 10h31M23 2l9 8-9 8" fill="none" stroke="#aaa" stroke-width="1.4"/></svg>
</div>
<div class="card" style="left:1038px">
  <div class="icon"><svg width="44" height="44" viewBox="0 0 44 44"><rect x="15" y="15" width="14" height="14" rx="2" fill="none" stroke="var(--red)" stroke-width="1.6"/><path d="M22 15V6M22 29v9M15 22H6M29 22h9M17 17l-7-7M27 17l7-7M17 27l-7 7M27 27l7 7" stroke="var(--red)" stroke-width="1.4"/><circle cx="22" cy="5" r="2" fill="var(--red)"/><circle cx="22" cy="39" r="2" fill="var(--red)"/><circle cx="5" cy="22" r="2" fill="var(--red)"/><circle cx="39" cy="22" r="2" fill="var(--red)"/></svg></div>
  <h3>Intelligence</h3>
  <p>Lorem ipsum dolor sit amet,<br>consectetur adipiscing elit seddo...</p>
  <svg class="go" width="34" height="20" viewBox="0 0 34 20"><path d="M1 10h31M23 2l9 8-9 8" fill="none" stroke="#aaa" stroke-width="1.4"/></svg>
</div>

<!-- BLUE PIKE -->
<div class="abs kicker" style="left:0;top:2073px;width:1200px;text-align:center">Blue Pike</div>
<h2 class="abs h2" style="left:0;top:2098px;width:1200px;text-align:center">Duis aute irure dolor in reprehenderit</h2>

<h3 class="abs h3" style="left:208px;top:2220px">Training</h3>
<p class="abs body" style="left:208px;top:2270px;width:290px">Velit esse cillum dolore eu fugiat nulla pariatur. Excepteur sint occaecat cupidatat non proident, sunt in culpa qui officia deserunt mollit anim id est laborum.</p>
<a class="btn btn-line" style="left:208px;top:2406px;width:104px;height:44px">Explore</a>
<div class="photo" style="left:567px;top:2197px;width:425px;height:284px;background:linear-gradient(135deg,#4a6078,#3a56a6 45%,#c9c3b4)" role="img" aria-label="Presenter with a tablet in front of a seated audience in a conference room"></div>

<svg class="abs" style="left:225px;top:2522px" width="310" height="375" viewBox="0 0 310 375" role="img" aria-label="Smiling man in a navy shirt reaching out for a handshake">
  <defs><linearGradient id="consultGrad" x1="0" y1="0" x2="0" y2="1"><stop offset="0" stop-color="#e9ddd2"/><stop offset=".3" stop-color="#3d4a63"/><stop offset="1" stop-color="#27324a"/></linearGradient></defs>
  <polygon points="90,40 220,40 310,150 310,280 235,375 75,375 0,280 0,150" fill="#f6f6f6"/>
  <rect x="40" y="20" width="230" height="355" rx="40" fill="url(#consultGrad)"/>
</svg>
<h3 class="abs h3" style="left:615px;top:2625px">Consulting</h3>
<p class="abs body" style="left:615px;top:2674px;width:360px">Velit esse cillum dolore eu fugiat nulla pariatur. Excepteur sint occaecat cupidatat non proident, sunt in culpa qui officia deserunt mollit anim id est laborum. Sed ut perspiciatis unde omnis iste natus error sit voluptatem accusantiu.</p>
<a class="btn btn-fill" style="left:615px;top:2810px;width:154px;height:44px">Need A Consult</a>

<!-- CONTACT -->
<div class="abs kicker" style="left:182px;top:3028px">Contact Us</div>
<h2 class="abs h2" style="left:182px;top:3054px;width:340px">Contact us for a quote,help or to join the team.</h2>
<div class="contact-row" style="top:3172px"><span class="dot-icon"><svg width="10" height="12" viewBox="0 0 10 12"><path d="M5 11S1 7 1 4.5a4 4 0 0 1 8 0C9 7 5 11 5 11Z" fill="none" stroke="#fff" stroke-width="1.2"/><circle cx="5" cy="4.5" r="1.3" fill="#fff"/></svg></span><span style="width:280px">1480 Linden Ave San Francisco, California(CA), 94118</span></div>
<div class="contact-row" style="top:3236px"><span class="dot-icon"><svg width="11" height="11" viewBox="0 0 11 11"><path d="M2 1h2l1 2.5-1.3 1a6 6 0 0 0 2.8 2.8l1-1.3L10 7v2c0 .6-.5 1-1 1A8 8 0 0 1 1 2c0-.5.4-1 1-1Z" fill="none" stroke="#fff" stroke-width="1.1"/></svg></span><span>(415) 555-0148</span></div>
<div class="contact-row" style="top:3283px"><span class="dot-icon"><svg width="12" height="9" viewBox="0 0 12 9"><rect x=".6" y=".6" width="10.8" height="7.8" fill="none" stroke="#fff" stroke-width="1.1"/><path d="m1 1 5 4 5-4" fill="none" stroke="#fff" stroke-width="1.1"/></svg></span><span>hello@valmikgroup.example</span></div>
<a class="btn btn-line" style="left:182px;top:3351px;width:166px;height:44px">Have A Question?</a>
<div class="photo" style="left:544px;top:2991px;width:568px;height:443px;background:linear-gradient(135deg,#a9dce0,#8ccfd6 60%,#7fc4cc)" role="img" aria-label="Cream telephone handset surrounded by paper speech bubbles on a light blue background"></div>

<!-- FOOTER -->
<svg class="footer-bg" width="1200" height="411" viewBox="0 0 1200 411">
  <path d="M0 100 Q560 -10 1200 40 L1200 411 L0 411Z" fill="var(--red-dark)"/>
  <path d="M0 118 Q560 20 1200 42 L1200 411 L0 411Z" fill="var(--black)"/>
</svg>
<div class="foot-brand"><span class="mark"></span><span class="name">VALMIK GROUP</span></div>

<div class="foot-title" style="left:445px;top:3616px">Quick Links</div>
<a class="foot-link" style="left:445px;top:3673px">Home</a>
<a class="foot-link" style="left:445px;top:3709px">About Us</a>
<a class="foot-link" style="left:445px;top:3745px">Services</a>
<a class="foot-link" style="left:445px;top:3782px">Blue Pike</a>
<a class="foot-link" style="left:589px;top:3673px">Contact Us</a>
<a class="foot-link" style="left:589px;top:3709px">Privacy &amp; Policy</a>
<a class="foot-link" style="left:589px;top:3745px">Trams &amp; Condition</a>

<div class="foot-title" style="left:785px;top:3616px">Subscribe</div>
<div class="subscribe"><span>Enter Your Email</span><b>Join</b></div>
<span class="social" style="left:788px"></span>
<span class="social" style="left:823px"></span>
<span class="social" style="left:859px"></span>
<span class="social" style="left:895px"></span>
<div class="foot-rule"></div>
<div class="copy">© copyright@ 2021 valmikgroup.example</div>

</body>
</html>
```